Harbor Lantern Vodka needs new design for its Chili Vodka line

use the existing label attached to add a chili aspect to the label for our new Chili Vodka.

Target Market(s)

high end

Requirements
Must have
• creative image
Nice to have
• red chili peppers
Should not have
• fire

```html
<!DOCTYPE html>
<html lang="en">
<head>
<meta charset="utf-8">
<title>Harbor Lantern Vodka – Red Chili Peppers Label</title>
<link rel="stylesheet" href="https://fonts.googleapis.com/css2?family=Barlow:wght@500;600;800&family=Barlow+Condensed:wght@700&display=swap">
<style>
  :root {
    --page: #eeeeee;
    --label: #ffffff;
    --gold: #c8962c;
    --gold-light: #e8c35a;
    --ink: #1a1a1a;
    --chili: #d8261c;
    --chili-dark: #8e0d0b;
    --banner: #8a0b0b;
  }
  * { margin: 0; padding: 0; box-sizing: border-box; }
  html, body {
    width: 960px; height: 1200px; overflow: hidden;
    background: var(--page);
  }
  .label {
    position: absolute; left: 90px; top: 50px;
    width: 780px; height: 1100px;
    background: var(--label);
    font-family: "Barlow", sans-serif;
    color: var(--ink);
  }
  .label__frame {
    position: absolute; inset: 14px;
    border: 3px solid var(--gold);
  }
  .distillery {
    position: absolute; top: 58px; left: 0; right: 0;
    text-align: center; font-size: 21px; font-weight: 500;
    letter-spacing: 0.5px;
  }
  .wordmark {
    position: absolute; top: 128px; left: 0; right: 0;
    text-align: center; color: var(--gold);
    font-weight: 600; line-height: 0.98; text-transform: uppercase;
  }
  .wordmark__line { display: block; }
  .wordmark__line--harbor { font-size: 150px; letter-spacing: 4px; }
  .wordmark__line--lantern { font-size: 128px; letter-spacing: 2px; }
  .wordmark__line--vodka { font-size: 112px; letter-spacing: 6px; }
  .tagline {
    position: absolute; top: 672px; left: 0; right: 0;
    text-align: center; font-size: 23px; font-weight: 500;
    letter-spacing: 4px;
  }
  .chili-art {
    position: absolute; left: 180px; top: 722px;
    width: 420px; height: 230px; border-radius: 115px / 90px;
    background: radial-gradient(ellipse at 55% 45%, var(--chili) 0%, #b51913 60%, var(--chili-dark) 100%);
  }
  .strength {
    position: absolute; left: 50px; top: 1010px;
    text-align: center; line-height: 1.05;
  }
  .strength__abv { font-family: "Barlow Condensed", sans-serif; font-size: 27px; }
  .strength__unit { font-size: 17px; font-weight: 500; }
  .flavour-banner {
    position: absolute; left: 150px; top: 1008px;
    width: 468px; height: 54px;
  }
  .flavour-banner text {
    font-family: "Barlow", sans-serif; font-weight: 800;
    font-size: 31px; fill: #ffffff; letter-spacing: 0.5px;
  }
  .volume {
    position: absolute; left: 648px; top: 1012px;
    font-family: "Barlow Condensed", sans-serif; font-size: 38px;
  }
</style>
</head>
<body>
  <main class="label">
    <div class="label__frame"></div>

    <p class="distillery">GRAY COVE DISTILLERY</p>

    <h1 class="wordmark">
      <span class="wordmark__line wordmark__line--harbor">Harbor</span>
      <span class="wordmark__line wordmark__line--lantern">Lantern</span>
      <span class="wordmark__line wordmark__line--vodka">Vodka</span>
    </h1>

    <p class="tagline">PREMIUM QUALITY</p>

    <div class="chili-art" role="img" aria-label="Illustration of a glossy red chili pepper with a green stem"></div>

    <div class="strength">
      <div class="strength__abv">40%</div>
      <div class="strength__unit">Alc/Vol</div>
    </div>

    <svg class="flavour-banner" viewBox="0 0 468 54" aria-label="Red Chili Peppers">
      <polygon points="0,0 468,0 452,27 468,54 0,54 16,27" fill="var(--banner)"/>
      <text x="234" y="38" text-anchor="middle">RED CHILI PEPPERS</text>
    </svg>

    <div class="volume">70cl</div>
  </main>
</body>
</html>
```